Design and Renovation Company Luxury Business Card

I want to create a luxury business card for a Design and Renovation Firm . We will use our current logo. The company name is 742BUILD. We do not want anything standard. We need a very unique concept.
Please see uploaded inspiration. I really like the textured paper option. I would like the card to be thick with debossing, and/or embossing options. The logo has orange in it but I would like to see the card with and without the orange. I think the orange may make the company feel less high-end. The goal is to elevate the logo not match its vibe per se of the logo. We want something very unique, not standard at all!
I would like a space for :
Logo,
Name,
Position,
Email,
Office number,
Website Address,
Business Address,
Thank you!
Have fun!
Target Market(s)
Home owners Age 35 +
Industry/Entity Type
Design and Renovation
Contact Information for Business Card
Logo, Name, Position, Email, Office number, Website Address, Business Address,.
Colors
Designer to choose colors to be used in the design.
Requirements
Must have
- A luxury designer feel. Must be black or dark grey but open to other luxury ideas.
Nice to have
- Gold, silver, black embossing or debossing. Textured paper design.
Should not have
- A cheap look and feel.

```html
<!DOCTYPE html>
<html lang="en">
<head>
<meta charset="utf-8">
<title>742BUILD Business Card</title>
<link rel="stylesheet" href="https://fonts.googleapis.com/css2?family=Barlow:wght@400;500&family=Barlow+Semi+Condensed:wght@600;700&family=Roboto:wght@400&display=swap">
<style>
  :root {
    --backdrop: #005081;
    --card: #0b0b10;
    --card-raised: #121217;
    --mark: #1d1d23;
    --name: #4b4b52;
    --detail: #56565d;
    --rule: #4b4b52;
  }
  * { margin: 0; padding: 0; box-sizing: border-box; }
  html, body {
    width: 1200px;
    height: 1000px;
    overflow: hidden;
    background: var(--backdrop);
  }
  .canvas { position: relative; width: 1200px; height: 1000px; }

  .card {
    position: absolute;
    left: 291px;
    width: 617px;
    height: 354px;
    background: var(--card);
    overflow: hidden;
  }
  .card--front { top: 122px; }
  .card--back { top: 525px; }

  /* front */
  .front-texture {
    position: absolute;
    inset: 0;
    background: linear-gradient(135deg, var(--card-raised) 0%, var(--card) 45%, var(--card-raised) 100%);
  }
  .brand-block {
    position: absolute;
    left: 118px;
    top: 124px;
    display: flex;
    align-items: flex-start;
    gap: 14px;
  }
  .brand-square {
    width: 62px;
    height: 64px;
    background: var(--mark);
  }
  .brand-name {
    font-family: "Barlow", sans-serif;
    font-weight: 500;
    font-size: 66px;
    line-height: 54px;
    letter-spacing: 3px;
    color: var(--mark);
  }
  .brand-tagline {
    display: block;
    margin-top: 10px;
    font-family: "Barlow", sans-serif;
    font-weight: 500;
    font-size: 14px;
    line-height: 14px;
    letter-spacing: 7.2px;
    color: var(--mark);
  }

  /* back */
  .holder {
    position: absolute;
    left: 56px;
    top: 86px;
  }
  .holder-name {
    font-family: "Barlow Semi Condensed", sans-serif;
    font-weight: 700;
    font-size: 39px;
    line-height: 38px;
    color: var(--name);
    letter-spacing: 0.5px;
  }
  .holder-role {
    display: flex;
    align-items: center;
    gap: 7px;
    margin-top: 2px;
    width: 230px;
  }
  .holder-role span {
    font-family: "Barlow Semi Condensed", sans-serif;
    font-weight: 700;
    font-size: 18px;
    line-height: 20px;
    color: var(--name);
    letter-spacing: 0.4px;
  }
  .holder-role svg { flex: 1; height: 2px; }

  .contact-list {
    position: absolute;
    left: 56px;
    top: 176px;
    list-style: none;
  }
  .contact-list li {
    font-family: "Roboto", sans-serif;
    font-size: 14px;
    line-height: 28.6px;
    color: var(--detail);
    letter-spacing: 0.3px;
  }

  .side-brand {
    position: absolute;
    left: 509px;
    top: 42px;
    display: flex;
    flex-direction: column;
    align-items: flex-end;
  }
  .side-square {
    width: 50px;
    height: 40px;
    background: var(--mark);
    margin-bottom: 8px;
  }
  .side-text {
    display: flex;
    flex-direction: row-reverse;
    gap: 4px;
  }
  .side-name {
    writing-mode: vertical-rl;
    font-family: "Barlow", sans-serif;
    font-weight: 500;
    font-size: 48px;
    line-height: 40px;
    letter-spacing: 2px;
    color: var(--mark);
  }
  .side-tagline {
    writing-mode: vertical-rl;
    font-family: "Barlow", sans-serif;
    font-weight: 500;
    font-size: 11px;
    line-height: 11px;
    letter-spacing: 5.2px;
    color: var(--mark);
  }
</style>
</head>
<body>
<main class="canvas">

  <section class="card card--front" aria-label="Card front">
    <div class="front-texture" role="img" aria-label="Faint debossed pattern of squares and vertical lines"></div>
    <div class="brand-block">
      <div class="brand-square"></div>
      <div>
        <div class="brand-name">742BUILD</div>
        <span class="brand-tagline">Design and Renovation Firm</span>
      </div>
    </div>
  </section>

  <section class="card card--back" aria-label="Card back">
    <div class="holder">
      <h1 class="holder-name">DANIEL REYES</h1>
      <div class="holder-role">
        <span>DIRECTOR</span>
        <svg viewBox="0 0 100 2" preserveAspectRatio="none" aria-hidden="true">
          <line x1="0" y1="1" x2="100" y2="1" stroke="var(--rule)" stroke-width="2"/>
        </svg>
      </div>
    </div>

    <ul class="contact-list">
      <li>48B, Harbor Ln, 60417.</li>
      <li>555-214-7730</li>
      <li>daniel@742build.com</li>
      <li>www.742build.com</li>
    </ul>

    <div class="side-brand">
      <div class="side-square"></div>
      <div class="side-text">
        <div class="side-name">742BUILD</div>
        <div class="side-tagline">Design and Renovation Firm</div>
      </div>
    </div>
  </section>

</main>
</body>
</html>
```